" A LÍVIA TORQUATO é uma empresa do ramo de decoração de casamentos. Há mais de uma década de trabalho, a empresa está passando por um momento de ressignificação do negócio, entre elas a atualização das marcas. No mundo da decoração, as empresas sempre se caracterizam por conceito e estilo. Atualmente a Lívia Torquato tem usado o conceito borró chique e clássico, podendo mudar sempre que houver uma nova tendência ou moda no mundo da decoração. A Lívia Torquato, além de proprietária, é a decoradora master da empresa. Um das principais características identificadas no modelo de atendimento e operações da empresa são: a sofisticação do eventos, comprometimento, responsabilidade, praticidade e solucionadoras de problemas. "

```html
<!DOCTYPE html>
<html lang="pt-BR">
<head>
<meta charset="UTF-8">
<title>Lívia Torquato — Cartão de visita</title>
<link rel="stylesheet" href="https://fonts.googleapis.com/css2?family=Montserrat:wght@400;600&family=Raleway:wght@300&display=swap">
<style>
  :root {
    --bg: #ececec;
    --card-white: #ffffff;
    --rose: #c9787c;
    --rose-deep: #b5575e;
    --rose-soft: #d99597;
    --ink: #4a4a4a;
    --ink-light: #6d6d6d;
    --on-rose: #ffffff;
  }
  * { margin: 0; padding: 0; box-sizing: border-box; }
  html, body { width: 1200px; height: 1200px; overflow: hidden; }
  body {
    background: var(--bg);
    font-family: "Montserrat", sans-serif;
    position: relative;
  }
  .card {
    position: absolute;
    width: 760px;
    height: 470px;
    border-radius: 34px;
    overflow: hidden;
    box-shadow: 0 12px 30px rgba(0,0,0,0.12);
  }
  /* Front */
  .card--front { left: 110px; top: 110px; background: var(--card-white); }
  .contact-block {
    position: absolute;
    left: 60px;
    top: 150px;
    border-left: 5px solid var(--rose-deep);
    padding-left: 16px;
  }
  .person-name {
    font-weight: 600;
    font-size: 30px;
    letter-spacing: 0.5px;
    color: var(--rose-deep);
    line-height: 1.1;
  }
  .person-role {
    font-size: 21px;
    color: var(--ink);
    margin-top: 2px;
  }
  .contact-list {
    list-style: none;
    margin-top: 22px;
    margin-left: -16px;
  }
  .contact-list li {
    display: flex;
    align-items: center;
    gap: 14px;
    font-size: 18px;
    color: var(--ink);
    height: 34px;
  }
  .contact-icon {
    width: 24px; height: 24px;
    flex: none;
  }
  .front-mark {
    position: absolute;
    right: 56px;
    top: 190px;
    display: flex;
    align-items: center;
    gap: 14px;
  }
  .mark-dot {
    width: 18px; height: 18px;
    border-radius: 50%;
    background: var(--rose);
  }
  .mark-name {
    font-family: "Raleway", sans-serif;
    font-weight: 300;
    font-size: 30px;
    letter-spacing: 2px;
    color: var(--ink-light);
    border-top: 2px solid var(--rose-soft);
    padding-top: 8px;
  }
  .front-tab {
    position: absolute;
    left: 310px;
    bottom: 0;
    width: 150px;
    height: 14px;
    background: var(--rose);
  }
  /* Back */
  .card--back { left: 330px; top: 620px; background: var(--rose); }
  .back-mark {
    position: absolute;
    left: 0; right: 0;
    top: 50%;
    transform: translateY(-50%);
    text-align: center;
  }
  .back-mark .mark-name {
    color: var(--on-rose);
    border-top: 2px solid var(--on-rose);
    font-size: 46px;
    letter-spacing: 3px;
    display: inline-block;
    padding-top: 12px;
  }
</style>
</head>
<body>
  <section class="card card--front" aria-label="Frente do cartão">
    <div class="contact-block">
      <h1 class="person-name">LÍVIA TORQUATO</h1>
      <p class="person-role">Diretora Comercial</p>
      <ul class="contact-list">
        <li>
          <svg class="contact-icon" viewBox="0 0 24 24"><circle cx="12" cy="12" r="12" fill="#c9787c"/><path d="M8.5 6.5l2 2-1.2 1.5a7 7 0 0 0 4.7 4.7l1.5-1.2 2 2-1.5 1.7c-4.5-.3-8.6-4.4-9-9z" fill="#fff"/></svg>
          (061) 97412-3058
        </li>
        <li>
          <svg class="contact-icon" viewBox="0 0 24 24"><circle cx="12" cy="12" r="12" fill="#c9787c"/></svg>
          @liviatorquato.decoracoes
        </li>
        <li>
          <svg class="contact-icon" viewBox="0 0 24 24"><circle cx="12" cy="12" r="12" fill="#c9787c"/><rect x="6" y="8" width="12" height="8" rx="1" fill="none" stroke="#fff" stroke-width="1.4"/><path d="M6 8.5l6 4.5 6-4.5" fill="none" stroke="#fff" stroke-width="1.4"/></svg>
          contato@liviatorquato.com.br
        </li>
        <li>
          <svg class="contact-icon" viewBox="0 0 24 24"><circle cx="12" cy="12" r="12" fill="#c9787c"/><circle cx="12" cy="12" r="6" fill="none" stroke="#fff" stroke-width="1.3"/><ellipse cx="12" cy="12" rx="2.6" ry="6" fill="none" stroke="#fff" stroke-width="1.3"/><path d="M6 12h12" stroke="#fff" stroke-width="1.3"/></svg>
          www.liviatorquato.com.br
        </li>
      </ul>
    </div>
    <div class="front-mark">
      <span class="mark-dot"></span>
      <span class="mark-name">LÍVIA TORQUATO</span>
    </div>
    <div class="front-tab"></div>
  </section>

  <section class="card card--back" aria-label="Verso do cartão">
    <div class="back-mark">
      <span class="mark-name">LÍVIA TORQUATO</span>
    </div>
  </section>
</body>
</html>
```